Business card based on your logo design "Marlowe&Co"

Can you please design a business card based on the logo artwork you designed for our business. Double sided as per your submitted image of possible application of logo.

```html
<!DOCTYPE html>
<html lang="en">
<head>
<meta charset="utf-8">
<title>Marlowe&amp;Co Business Card</title>
<link rel="stylesheet" href="https://fonts.googleapis.com/css2?family=Roboto:wght@400;500;700&family=Roboto+Condensed:wght@700&display=swap">
<style>
  :root {
    --stage: #ececec;
    --card: #f7f7f6;
    --ink: #2e2e2e;
    --ink-soft: #555555;
    --accent: #e08a12;
    --divider: #dcdcdc;
  }
  * { box-sizing: border-box; margin: 0; padding: 0; }
  html, body {
    width: 1200px; height: 1001px; overflow: hidden;
    background: var(--stage);
    font-family: "Roboto", Arial, sans-serif;
    color: var(--ink);
  }
  .stage { position: relative; width: 1200px; height: 1001px; }
  .card {
    position: absolute;
    width: 560px; height: 320px;
    background: var(--card);
    box-shadow: 0 10px 28px rgba(0,0,0,.12), 0 2px 4px rgba(0,0,0,.08);
  }
  .card--front { left: 560px; top: 150px; }
  .card--back { left: 80px; top: 531px; overflow: hidden; }

  .brand { display: flex; align-items: center; gap: 14px; }
  .brand__mark { width: 18px; height: 18px; background: var(--accent); flex: none; }
  .brand__name {
    font-family: "Roboto Condensed", "Roboto", Arial, sans-serif;
    font-weight: 700; text-transform: uppercase;
    color: var(--ink); letter-spacing: 1px; line-height: 1;
  }
  .brand__tagline {
    font-size: 12px; letter-spacing: 2px; color: var(--ink-soft);
    margin-top: 10px;
  }

  .card--front .lockup { position: absolute; left: 70px; top: 108px; }
  .card--front .brand__name { font-size: 64px; }
  .card--front .brand__tagline { font-size: 14px; margin-left: 32px; }

  .card--back .lockup { position: absolute; left: 30px; top: 112px; }
  .card--back .brand__mark { width: 11px; height: 11px; }
  .card--back .brand { gap: 9px; }
  .card--back .brand__name { font-size: 36px; }
  .card--back .brand__tagline { font-size: 9px; letter-spacing: 1.4px; margin-left: 20px; margin-top: 7px; }

  .card__divider { position: absolute; inset: 0; pointer-events: none; }

  .contact { position: absolute; left: 318px; top: 78px; width: 220px; }
  .contact__name { color: var(--accent); font-weight: 700; font-size: 17px; }
  .contact__role { font-size: 14px; font-weight: 500; margin-top: 3px; }
  .contact__rule { height: 2px; background: var(--accent); margin: 9px 0 12px; }
  .contact__rule--end { margin: 12px 0 0; }
  .contact__list { list-style: none; }
  .contact__item {
    display: flex; align-items: flex-start; gap: 8px;
    font-size: 11.5px; line-height: 1.3; margin-bottom: 4px;
  }
  .contact__icon { width: 12px; height: 12px; flex: none; margin-top: 1px; fill: var(--accent); }
</style>
</head>
<body>
<main class="stage">

  <section class="card card--front" aria-label="Card front">
    <div class="lockup">
      <div class="brand">
        <span class="brand__mark"></span>
        <span class="brand__name">Marlowe&amp;Co</span>
      </div>
      <p class="brand__tagline">Building and Project Management</p>
    </div>
  </section>

  <section class="card card--back" aria-label="Card back">
    <svg class="card__divider" width="560" height="320" viewBox="0 0 560 320">
      <line x1="330" y1="0" x2="278" y2="320" stroke="var(--divider)" stroke-width="1.5"/>
    </svg>

    <div class="lockup">
      <div class="brand">
        <span class="brand__mark"></span>
        <span class="brand__name">Marlowe&amp;Co</span>
      </div>
      <p class="brand__tagline">Building and Project Management</p>
    </div>

    <div class="contact">
      <p class="contact__name">Your Name</p>
      <p class="contact__role">Owner and CEO</p>
      <div class="contact__rule"></div>
      <ul class="contact__list">
        <li class="contact__item">
          <svg class="contact__icon" viewBox="0 0 12 12"><path d="M6 0a4 4 0 0 0-4 4c0 3 4 8 4 8s4-5 4-8a4 4 0 0 0-4-4zm0 5.5A1.5 1.5 0 1 1 6 2.5a1.5 1.5 0 0 1 0 3z"/></svg>
          <span>Your long address commercial or domestic</span>
        </li>
        <li class="contact__item">
          <svg class="contact__icon" viewBox="0 0 12 12"><path d="M2.5 1l2 2.2-1 1.3c.8 1.6 2 2.8 3.6 3.6l1.3-1 2.2 2-1.3 1.6C5 10.4 1.6 7 .9 2.3z"/></svg>
          <span>0000.1122.3344</span>
        </li>
        <li class="contact__item">
          <svg class="contact__icon" viewBox="0 0 12 12"><path d="M0 2h12v8H0zm1 1v.4l5 3.3 5-3.3V3z" fill-rule="evenodd"/></svg>
          <span>yourname@yourwebsite.com</span>
        </li>
        <li class="contact__item">
          <svg class="contact__icon" viewBox="0 0 12 12"><circle cx="6" cy="6" r="5.5"/><path d="M.5 6h11M6 .5c-3 3-3 8 0 11M6 .5c3 3 3 8 0 11M1.5 3.3h9M1.5 8.7h9" stroke="var(--card)" stroke-width=".8" fill="none"/></svg>
          <span>www.yourwebsite.com</span>
        </li>
      </ul>
      <div class="contact__rule contact__rule--end"></div>
    </div>
  </section>

</main>
</body>
</html>
```